Website for a financial survey consultancy

WHO WE ARE
We're a niche HR consultancy specialising in salary comparison surveys for the financial asset management industry. We position ourselves as a small, highly responsive organisation with a strong personal relationship with each of our 50+ blue-chip clients.

WHAT WE DO
Our business is 80% surveys (= products), 20% consultancy (= services). The surveys are a set of online products which clients interact with to find the information they are interested in.

WHAT WE WANT
We are completely revising our existing marketing website and need a new up-to-date look and feel for the site. We want you to design 2 web pages
- Home page
- Internal content page

More details below in Must Have Priorities.

REFERENCE SITES
- www.tallowmere.com - nice background image
- www.quimbelt.com - ignoring the animations
- www.palvastro.com
- www.dulmiko.com - clean, fresh, styly but prob not corporate enough
- www.orvettagrove.com - spacious, beautiful, slightly dated tho
- www.plinzer.co.uk - ignore the colours. Like the simplicity, larger font size (although want to stick with sans-serif fonts for main content)

DELIVERABLES
The final designs should be delivered as one or more PSD files with clearly named layers. All design elements and treatments should be separated out, for example use adjustment layers rather than applied (and subsequently irreversible) adjustments, strokes, shading, etc.

WHAT NEXT
I'll be monitoring the contest every day and can respond to questions fast. You can IM me on Skype or MSN.

Reason: Hi folks,

I am extending the deadline to this project as I am travelling this week and therefore will not be able to make a final decision until next Monday. I will try and provide further feedback over the course of this week but I am only going to be online occasionally so be prepared to wait a few days for a reply from me.

Thanks for all the designs so far.

Owen

Target Market(s)

In order of importance, most important first

1. Potential customers - UK & US financial industry HR professionals, short on time. Heard about us already, want to find out more about what we do, confirm relevance for their needs. Core goal - establish credibility: are we properly resourced, will we be around for years to come, are we *real*.

2. Existing customers - UK & US financial industry professionals, short on time, under pressure, want results quickly, minimum faff, expect high quality, slickly presented information. Primary action: login and use surveys.

3. Industry professionals/researchers - probably arriving through blog content, looking to browse and hoover information. Valuable for their ability to spread awareness of who we are amongst their peers.

Industry/Entity Type

Financial

Requirements
Must have
• GENERAL
Style cues - Corporate, professional, financial, stylish, slick, clean, spacious, light
Size - standard 960px grid

NAVIGATION
- [ Home | About us | Surveys | Consulting | Blog ]
- Sub-nav (roll-over dropdown) on About Us, Surveys & Consulting

ALL PAGES
- Site navigation
- Client login (on screen permanently or link to ajaxy in-page pop-up)
- Footer section
- Existing logo (attached)* - this is obviously an important reference point in the design, esp colour

HOME PAGE
- Communicate (link thru to?) survey/consulting split
- Large photo(s)/backdrop (2-3 interchangeable options ideally). Please consider what rights agreement will be necessary for any photos you include in your design.
- Possibly bigger more prominent version of logo
- Strap line/sentence - "Focussed data is the key to success"
- 3 recent blog posts (should look good with and without blog post images)
- Free downloadable PDF research report + supporting blurb

INTERNAL PAGE
- Page title
- Content - typical page will be less than one screenfull
- Level 1 sub-heading
- Level 2 sub-heading
- Bulleted list
- Content supporting image (any image will do - interested in placement, borders (if any), spacing, caption, etc)
- 'Do something' button

* Note: there is some internal debate about this logo at the moment. Some (me) are keen for it to change, some (not me!) are not. If you have an web page design idea/concept that requires an evolution of the logo, go ahead and evolve it. We can explore this further in the design process as necessary, but don't sweat it.
Nice to have
• Values to communicate
- Knowledgeable
- Professional
- Secure
- Personal
- Experienced
- Financial industry specific
- Accurate
- Reliable
Should not have
• - Search box
- Social media links, other than RSS feed button (discrete)

```html
<!DOCTYPE html>
<html lang="en">
<head>
<meta charset="utf-8">
<title>Arvenel – HR consultancy</title>
<link rel="stylesheet" href="https://fonts.googleapis.com/css2?family=Noto+Sans:wght@400;700&family=Archivo+Narrow:wght@400;500&display=swap">
<style>
  :root {
    --page-bg: #e0e0e0;
    --brand-red: #6b0a0a;
    --nav-red: rgba(110, 30, 30, 0.85);
    --nav-active: #1f0906;
    --ink: #111111;
    --body-ink: #333333;
    --beige: #e6d6bf;
    --beige-line: #dccab4;
    --footer-bg: #030a10;
    --footer-ink: #f2f2f2;
    --accent-orange: #d2451e;
  }
  * { box-sizing: border-box; margin: 0; padding: 0; }
  html, body { width: 1200px; height: 900px; overflow: hidden; }
  body { background: var(--page-bg); font-family: "Noto Sans", Verdana, sans-serif; position: relative; }

  .site { position: absolute; left: 121px; top: 19px; width: 964px; height: 865px; }

  .hero {
    position: absolute; left: 0; top: 0; width: 964px; height: 653px;
    background:
      linear-gradient(155deg, rgba(255,255,255,0) 40%, rgba(240,236,228,0.9) 62%, rgba(250,248,244,0.95) 100%),
      linear-gradient(180deg, #cfdbe8 0%, #e6ebf0 45%, #f1f1ef 100%);
  }

  .brand-name {
    position: absolute; left: 45px; top: 110px;
    font-size: 24px; font-weight: 700; color: var(--brand-red); letter-spacing: 0.5px;
  }

  .client-login { position: absolute; right: 29px; top: 30px; font-size: 12px; color: var(--brand-red); text-decoration: underline; }

  .main-nav { position: absolute; left: 277px; top: 114px; display: flex; gap: 1px; }
  .main-nav a {
    width: 131px; height: 41px; line-height: 41px; text-align: center;
    background: var(--nav-red); color: #fff; font-size: 12px; font-weight: 700;
    text-decoration: none; text-transform: uppercase;
  }
  .main-nav a.is-active { background: var(--nav-active); }

  .headline {
    position: absolute; left: 27px; top: 418px;
    font-family: "Archivo Narrow", "Arial Narrow", sans-serif; font-weight: 400;
    font-size: 82px; line-height: 1; color: var(--ink); letter-spacing: 0.3px;
  }
  .strapline {
    position: absolute; left: 31px; top: 492px;
    font-family: "Archivo Narrow", "Arial Narrow", sans-serif; font-size: 30px; line-height: 1.2; color: var(--brand-red);
  }

  .latest-blogs {
    position: absolute; left: 610px; top: 217px; width: 324px; height: 304px;
    background: rgba(255,255,255,0.88); border: 3px solid var(--beige-line); padding: 11px 17px 0 17px;
  }
  .latest-blogs h2 {
    font-family: "Archivo Narrow", "Arial Narrow", sans-serif; font-weight: 400;
    font-size: 22px; line-height: 26px; color: var(--brand-red); padding-bottom: 4px;
    border-bottom: 4px solid var(--beige-line); margin-bottom: 10px;
  }
  .blog-post { margin-bottom: 15px; }
  .blog-post p { font-size: 11px; font-weight: 700; line-height: 13.5px; color: var(--body-ink); text-align: justify; }
  .read-more { display: inline-block; margin-top: 8px; font-size: 11px; line-height: 13px; color: var(--ink); text-decoration: underline; }
  .read-more::after { content: " »"; color: var(--accent-orange); display: inline-block; margin-left: 3px; font-weight: 700; }

  .report-download {
    position: absolute; left: 615px; top: 569px; width: 314px; height: 49px;
    background: linear-gradient(180deg, #f7efe4 0%, #dcc7ac 100%);
    border: 2px solid #efe3d3; display: flex; align-items: center; padding-left: 4px; text-decoration: none;
  }
  .report-icon { width: 40px; height: 40px; background: #c4161c; margin-right: 8px; flex: none; }
  .report-title { font-family: "Archivo Narrow", "Arial Narrow", sans-serif; font-size: 19px; color: #6b4a38; line-height: 1; }
  .report-sub { font-size: 12px; color: var(--brand-red); }

  .site-footer { position: absolute; left: 0; top: 653px; width: 964px; height: 212px; background: var(--footer-bg); color: var(--footer-ink); }
  .footer-col { position: absolute; top: 25px; }
  .footer-tab { width: 91px; height: 34px; line-height: 33px; text-align: center; background: var(--beige); color: var(--ink); font-size: 13px; }
  .footer-text { font-size: 12px; line-height: 16px; text-align: justify; }
  .col-about { left: 36px; }
  .col-about .footer-text { width: 172px; margin-top: 26px; }
  .col-surveys { left: 276px; }
  .col-consulting { left: 536px; }
  .footer-feature { display: flex; margin-top: 26px; }
  .footer-thumb { width: 70px; height: 70px; border: 3px solid #9a9a9a; flex: none; }
  .thumb-surveys { background: linear-gradient(180deg, #d8dde3, #8a96a8); margin-left: 2px; }
  .thumb-consulting { background: linear-gradient(180deg, #c9c3bb, #8b7c6e); margin-left: 1px; }
  .footer-feature .footer-text { margin-left: 10px; width: 139px; }
  .col-surveys .footer-text { text-align: left; }
  .learn-more { position: absolute; top: 151px; font-size: 12px; color: var(--footer-ink); text-decoration: none; }
  .learn-more::after { content: " ››"; font-weight: 700; }
  .col-surveys .learn-more { left: 83px; }
  .col-consulting .learn-more { left: 81px; }

  .footer-brand { position: absolute; left: 850px; top: 94px; font-size: 18px; font-weight: 700; color: #b03030; }
  .copyright { position: absolute; right: 5px; bottom: 7px; font-size: 11px; color: #cfcfcf; }
</style>
</head>
<body>
<div class="site">
  <header class="hero" role="img" aria-label="Large backdrop photo of a white cable-stayed bridge arch against a pale sky">
    <div class="brand-name">Arvenel</div>
    <a class="client-login" href="#">Client LOGIN</a>
    <nav class="main-nav">
      <a class="is-active" href="#">Home</a>
      <a href="#">About us</a>
      <a href="#">Surveys</a>
      <a href="#">Consulting</a>
      <a href="#">Blog</a>
    </nav>

    <h1 class="headline">HR consultancy</h1>
    <p class="strapline">Focussed data is the key to success</p>

    <section class="latest-blogs">
      <h2>Latest Blogs</h2>
      <article class="blog-post">
        <p>Lorem ipsum dolor sit amet, consectetur adipiscing elit. Integer fringilla sapien ligula. In hac habitasse platea dictumst.</p>
        <a class="read-more" href="#">Read More</a>
      </article>
      <article class="blog-post">
        <p>Lorem ipsum dolor sit amet, consectetur adipiscing elit. Integer fringilla sapien ligula. In hac habitasse platea dictumst.</p>
        <a class="read-more" href="#">Read More</a>
      </article>
      <article class="blog-post">
        <p>Lorem ipsum dolor sit amet, consectetur adipiscing elit. Integer fringilla sapien ligula. In hac habitasse platea dictumst.</p>
        <a class="read-more" href="#">Read More</a>
      </article>
    </section>

    <a class="report-download" href="#">
      <span class="report-icon"></span>
      <span>
        <span class="report-title">Research Report + Supporting Blurb</span><br>
        <span class="report-sub">Download PDF file</span>
      </span>
    </a>
  </header>

  <footer class="site-footer">
    <div class="footer-col col-about">
      <div class="footer-tab">About us</div>
      <p class="footer-text">Lorem ipsum dolor sit amet, consectetur adipiscing elit. Cras ante dui, viverra non vehicula in, condimentum id ipsum. Fusce at arcu metus.</p>
    </div>
    <div class="footer-col col-surveys">
      <div class="footer-tab">Surveys</div>
      <div class="footer-feature">
        <div class="footer-thumb thumb-surveys" role="img" aria-label="Photo of a businessman sitting with a laptop"></div>
        <p class="footer-text">Lorem ipsum dolor sit amet, consectetur adipiscing elit. Cras ante dui, viverra non vehicula in, condimentum</p>
      </div>
      <a class="learn-more" href="#">Learn More</a>
    </div>
    <div class="footer-col col-consulting">
      <div class="footer-tab">Consulting</div>
      <div class="footer-feature">
        <div class="footer-thumb thumb-consulting" role="img" aria-label="Photo of a businesswoman shaking hands"></div>
        <p class="footer-text">Fusce at arcu metus. eu justo nisl. Maecenas con-sequat condimentum ante, quis tincidunt neque viverra sed.</p>
      </div>
      <a class="learn-more" href="#">Learn More</a>
    </div>
    <div class="footer-brand">Arvenel</div>
    <p class="copyright">© 2011 Arvenel. All rights reserved</p>
  </footer>
</div>
</body>
</html>
```